Scripture-Rooted Covenant Church of Willow Crossing 2024 Theme

We, Scripture-Rooted Covenant Church of Willow Crossing, need a design for two banners; (1) a Horizontal 6' x 4' banner that will be placed on one wall in the main sanctuary, (2) a retractable banner. The banners are to communicate/advertise the church's theme for 2024, "Endeavoring to Grow, Know and Love God More in 2024" (2 Timothy 2:15). The design should include our logo and church name. Use the color purple. This banner should be reflective of growth, knowledge, love of God. Our congregation demographic is 98% African American, 2% Hispanic. Our home base is Tampa, Florida (USA), but we have a small social media following.

Target Market(s)

Church members and visitors; male and female ages 1-99

Industry/Entity Type

Religious

Colors
6B429C
8869AF
B7A5CE
E3DAEB
F3F0F8

Requirements
Must have
• Church logo, color purple
Nice to have
• Vibrant design; colors that complement purple

```html
<!DOCTYPE html>
<html lang="en">
<head>
<meta charset="utf-8">
<title>Scripture-Rooted Covenant Church of Willow Crossing – 2024 Theme Banners</title>
<link href="https://fonts.googleapis.com/css2?family=Fira+Sans:ital,wght@0,300;0,700;1,300&family=Montserrat:wght@600&display=swap" rel="stylesheet">
<style>
  :root{
    --backdrop:#a7a8a3;
    --ink:#000000;
    --purple:#6b459c;
    --lavender:#e3daeb;
    --mist:#b7a5ce;
    --white:#ffffff;
  }
  *{margin:0;padding:0;box-sizing:border-box}
  html,body{width:1200px;height:560px;overflow:hidden;background:var(--backdrop)}
  .canvas{position:relative;width:1200px;height:560px}

  .banner{position:absolute;overflow:hidden;background:var(--purple);color:var(--white)}
  .banner__waves{position:absolute;inset:0;width:100%;height:100%;display:block}

  .brand{position:absolute;display:flex;align-items:center;gap:6px}
  .brand__dot{flex:none;border-radius:50%;background:var(--mist)}
  .brand__name{font-family:"Montserrat",sans-serif;font-weight:600;color:var(--white);line-height:1.15}

  .church-name{position:absolute;font-family:"Montserrat",sans-serif;font-weight:600;line-height:1.3}

  .artwork{position:absolute;background:linear-gradient(180deg,#5e9a3a 0%,#3f7a2a 45%,#5a3b22 68%,#f3f0f8 82%,#d9d4de 100%);border-radius:4px}

  .theme{position:absolute;left:0;right:0;text-align:center;font-family:"Fira Sans",sans-serif;font-weight:300;line-height:1.12}
  .theme b{font-weight:700}
  .verse{position:absolute;font-family:"Fira Sans",sans-serif;font-weight:300;font-style:italic}

  /* horizontal wall banner */
  .banner--wall{left:74px;top:53px;width:682px;height:454px}
  .banner--wall .brand{left:40px;top:36px;width:140px}
  .banner--wall .brand__dot{width:30px;height:30px}
  .banner--wall .brand__name{font-size:10px}
  .banner--wall .church-name{left:193px;top:44px;font-size:15px}
  .banner--wall .artwork{left:212px;top:90px;width:260px;height:186px}
  .banner--wall .theme{top:280px;font-size:42px;line-height:47px}
  .banner--wall .verse{left:200px;top:372px;font-size:38px}

  /* retractable banner */
  .banner--rollup{left:883px;top:99px;width:165px;height:348px}
  .banner--rollup .brand{left:38px;top:28px;width:92px}
  .banner--rollup .brand__dot{width:18px;height:18px}
  .banner--rollup .brand__name{font-size:6.5px}
  .banner--rollup .church-name{left:0;right:0;top:88px;text-align:center;font-size:7.6px}
  .banner--rollup .artwork{left:30px;top:113px;width:110px;height:88px}
  .banner--rollup .theme{top:205px;font-size:17px;line-height:22px;padding:0 6px}
  .banner--rollup .verse{left:0;right:0;top:302px;text-align:center;font-size:14px}
</style>
</head>
<body>
<main class="canvas">

  <section class="banner banner--wall" aria-label="Horizontal sanctuary wall banner">
    <svg class="banner__waves" viewBox="0 0 682 454" preserveAspectRatio="none" aria-hidden="true">
      <rect width="682" height="454" fill="var(--ink)"/>
      <path d="M0 164 C150 140 260 120 380 108 C500 92 600 80 682 96 L682 454 L0 454 Z" fill="var(--lavender)"/>
      <path d="M0 204 C170 170 300 150 420 162 C540 172 620 160 682 155 L682 454 L0 454 Z" fill="var(--purple)"/>
    </svg>
    <div class="brand">
      <span class="brand__dot"></span>
      <span class="brand__name">Scripture-Rooted Covenant Church</span>
    </div>
    <p class="church-name">Scripture-Rooted Covenant Church of Willow Crossing,<br>Florida (USA)</p>
    <div class="artwork" role="img" aria-label="Young green plant growing from a mound of soil on an open book"></div>
    <h1 class="theme">Endeavoring to <b>Grow, Know</b><br>and <b>Love God</b> More in <b>2024</b></h1>
    <p class="verse">(2 Timothy 2:15)</p>
  </section>

  <section class="banner banner--rollup" aria-label="Retractable banner">
    <svg class="banner__waves" viewBox="0 0 165 348" preserveAspectRatio="none" aria-hidden="true">
      <rect width="165" height="348" fill="var(--ink)"/>
      <path d="M0 152 C40 150 80 132 120 130 C140 129 155 131 165 133 L165 348 L0 348 Z" fill="var(--lavender)"/>
      <path d="M0 160 C45 156 90 148 120 150 C140 151 155 152 165 153 L165 348 L0 348 Z" fill="var(--purple)"/>
    </svg>
    <div class="brand">
      <span class="brand__dot"></span>
      <span class="brand__name">Scripture-Rooted Covenant Church</span>
    </div>
    <p class="church-name">Scripture-Rooted Covenant Church<br>of Willow Crossing, Florida (USA)</p>
    <div class="artwork" role="img" aria-label="Young green plant growing from a mound of soil on an open book"></div>
    <h2 class="theme">Endeavoring to <b>Grow, Know</b> and <b>Love God</b> More in <b>2024</b></h2>
    <p class="verse">(2 Timothy 2:15)</p>
  </section>

</main>
</body>
</html>
```